family chiropractic health care team needs a modern business card design

Healthcare office with Chiropractors, Physiotherapists, Massage therapists and possibly other practitioners in the future. This is a friendly family office with patients of all ages (and lots of kids) that just moved into a new larger modern office.
Look at the website for photos of the office.
Design for the front and back of a business card required.
Text for the front:
Office logo and name of the office:
Bright Path Wellness Centre
Name of current Practitioner:
Dr. Marten Quovel B.Sc., D.C. Chiropractor
(But please include options to swap out name and title for other practitioners )

address:
218 Farrow Gate
Etobicoke ON.
K2J 6P4
Phone: 416-872-0196 (PATH)
Web site and email:
www.brightpathwellnesscentre.example
brightpathchiro@mailbox.example

2 versions of the back of the card:
1. text below
2. appointment schedule card

Text on back of card:
Chiropractic Card text on back of the card:
There is more to chiropractic than the relief of headaches and back pain! Our primary focus is the integrity of your nerve system, which controls and regulates every cell and tissue of your body. The moving bones of the spinal column can impair this vital communication link between your brain and body. We help improve the function and structure of your spine, reducing nerve system compromise. The result?
Even non-spinal related health problems can show improvement
without drugs
without surgery
regardless of age
for over a century
naturally

Appointment Card info For Back:
Please integrate design elements from the front of the card into an appointment card format.
M Tu W Th F Sat (and a line for writing on beside each one)

```html
<!DOCTYPE html>
<html lang="en">
<head>
<meta charset="utf-8">
<title>Bright Path Wellness Centre – Business Card</title>
<link rel="stylesheet" href="https://fonts.googleapis.com/css2?family=Arimo:wght@400;700&display=swap">
<style>
  :root {
    --backdrop: #cbcac6;
    --card-dark: #1c1c1c;
    --card-light: #ffffff;
    --leaf-green: #8cc63f;
    --ink: #222222;
    --ink-soft: #3a3a3a;
    --rule: #1f1f1f;
    --white: #ffffff;
  }
  * { margin: 0; padding: 0; box-sizing: border-box; }
  html, body {
    width: 1200px; height: 801px; overflow: hidden;
    background: var(--backdrop);
    font-family: "Arimo", Arial, sans-serif;
  }
  .sheet {
    width: 1200px; height: 801px;
    display: flex; align-items: center; justify-content: center; gap: 40px;
  }
  .card {
    position: relative;
    width: 540px; height: 309px;
    box-shadow: 0 10px 24px rgba(0,0,0,0.25);
    overflow: hidden;
  }

  /* Front */
  .card--front { background: var(--card-dark); color: var(--white); }
  .brand {
    position: absolute; left: 40px; top: 42px;
    display: flex; align-items: center; gap: 14px;
  }
  .brand__dot {
    width: 34px; height: 34px; border-radius: 50%;
    background: var(--leaf-green);
  }
  .brand__name {
    color: var(--leaf-green);
    font-weight: 700; font-size: 30px; line-height: 1.05;
    letter-spacing: 0.5px; width: 300px;
  }
  .address-band {
    position: absolute; left: 0; right: 0; top: 150px; height: 30px;
    background: var(--white); color: var(--ink);
    font-weight: 700; font-size: 15px;
    display: flex; align-items: center; padding-left: 40px;
    word-spacing: 2px;
  }
  .practitioner {
    position: absolute; left: 40px; top: 220px;
  }
  .practitioner__name {
    color: var(--leaf-green); font-size: 20px; font-weight: 400;
  }
  .practitioner__title {
    font-size: 11px; margin-top: 4px; color: var(--white);
  }
  .divider {
    position: absolute; left: 268px; top: 208px;
    width: 1px; height: 56px; background: var(--white);
  }
  .contacts {
    position: absolute; left: 290px; top: 204px;
    list-style: none; font-size: 13px; line-height: 21px;
  }
  .contacts li { display: flex; align-items: center; gap: 8px; }
  .contacts svg { width: 12px; height: 12px; fill: var(--white); flex: none; }

  /* Back */
  .card--back { background: var(--card-light); color: var(--ink); }
  .claims {
    position: absolute; left: 60px; top: 30px; font-size: 13px; line-height: 16px;
  }
  .claims__lead { margin-bottom: 3px; }
  .claims__list { list-style: none; padding-left: 84px; }
  .claims__list li::before {
    content: "\25B6"; font-size: 9px; margin-right: 7px; vertical-align: 1px;
  }
  .appointments {
    position: absolute; left: 40px; top: 150px; right: 40px;
  }
  .appointments__label { font-size: 15px; margin-bottom: 10px; }
  .slot {
    display: flex; align-items: flex-end; height: 23px; font-size: 15px;
  }
  .slot__day { width: 46px; }
  .slot__line { flex: 1; border-bottom: 1px solid var(--rule); margin-bottom: 4px; }
  .slot__ampm { font-size: 11px; margin-left: 6px; margin-bottom: 2px; color: var(--ink-soft); }
</style>
</head>
<body>
<main class="sheet">

  <section class="card card--front" aria-label="Business card front">
    <div class="brand">
      <span class="brand__dot"></span>
      <span class="brand__name">Bright Path Wellness Centre</span>
    </div>

    <div class="address-band">218 Farrow Gate&nbsp; Etobicoke ON. K2J 6P4</div>

    <div class="practitioner">
      <p class="practitioner__name">Dr. Marten Quovel</p>
      <p class="practitioner__title">B.Sc., D.C. Chiropractor</p>
    </div>

    <span class="divider"></span>

    <ul class="contacts">
      <li>
        <svg viewBox="0 0 24 24" aria-hidden="true"><path d="M6.6 10.8a15 15 0 0 0 6.6 6.6l2.2-2.2c.3-.3.7-.4 1-.2 1.1.4 2.3.6 3.6.6.6 0 1 .4 1 1V20c0 .6-.4 1-1 1A17 17 0 0 1 3 4c0-.6.4-1 1-1h3.5c.6 0 1 .4 1 1 0 1.3.2 2.5.6 3.6.1.3 0 .7-.2 1z"/></svg>
        416-872-0196
      </li>
      <li>
        <svg viewBox="0 0 24 24" aria-hidden="true"><path d="M12 2a10 10 0 1 0 0 20 10 10 0 0 0 0-20zm6.9 6h-3a15 15 0 0 0-1.3-3.9A8 8 0 0 1 18.9 8zM12 4c.8 1.2 1.5 2.5 1.9 4h-3.8c.4-1.4 1.1-2.8 1.9-4zM4.3 14a8 8 0 0 1 0-4h3.4a16 16 0 0 0 0 4zm.8 2h3a15 15 0 0 0 1.3 3.9A8 8 0 0 1 5.1 16zm3-8h-3a8 8 0 0 1 4.3-3.9C8.8 5.3 8.4 6.6 8.1 8zM12 20c-.8-1.2-1.5-2.5-1.9-4h3.8c-.4 1.4-1.1 2.8-1.9 4zm2.3-6H9.7a14 14 0 0 1 0-4h4.6a14 14 0 0 1 0 4zm.3 5.9c.6-1.2 1-2.5 1.3-3.9h3a8 8 0 0 1-4.3 3.9zM16.3 14a16 16 0 0 0 0-4h3.4a8 8 0 0 1 0 4z"/></svg>
        www.brightpathwellnesscentre.example
      </li>
      <li>
        <svg viewBox="0 0 24 24" aria-hidden="true"><path d="M2 5h20v14H2zm2 2v.5l8 5 8-5V7l-8 5z"/></svg>
        brightpathchiro@mailbox.example
      </li>
    </ul>
  </section>

  <section class="card card--back" aria-label="Business card back, appointment card">
    <div class="claims">
      <p class="claims__lead">Even non-spinal related health problems can show improvement</p>
      <ul class="claims__list">
        <li>without drugs</li>
        <li>without surgery</li>
        <li>regardless of age for over a century</li>
        <li>naturally</li>
      </ul>
    </div>

    <div class="appointments">
      <p class="appointments__label">Appointments :</p>
      <div class="slot"><span class="slot__day">Mon</span><span class="slot__line"></span><span class="slot__ampm">am / pm</span></div>
      <div class="slot"><span class="slot__day">Tue</span><span class="slot__line"></span><span class="slot__ampm">am / pm</span></div>
      <div class="slot"><span class="slot__day">Wed</span><span class="slot__line"></span><span class="slot__ampm">am / pm</span></div>
      <div class="slot"><span class="slot__day">Thu</span><span class="slot__line"></span><span class="slot__ampm">am / pm</span></div>
      <div class="slot"><span class="slot__day">Sat</span><span class="slot__line"></span><span class="slot__ampm">am / pm</span></div>
    </div>
  </section>

</main>
</body>
</html>
```